Children Online Clothing Business Needs a Facebook Design

We need a facebook design (including facebook banner and profile picture) for a new company based in Australia called "Dress Up Poppet". We are an online clothing company specializing in unique, stylish and fun clothing for children (primarily girls). The final design should be stylish and eye catching and communicate childhood with a feeling of fun, carefree and whimsical.

Target Market(s)

Primarily mums of young children

Industry/Entity Type

Clothing

Requirements
Must have
• The company name "Dress Up Poppet"
The company slogan "Out of her dreams and into her wardrobe"
Images that represent childhood (examples would be rainbows, clouds, stars, swings, nature, girl dressed in tutu or anything else you can think of).
I require a facebook banner image as well as logo/profile picture that can be used for facebook.
Should not have
• No images of actual children. However silhouette's or drawings of children would be good. The reason I do not want actual children is that they will not be wearing the clothes that we will be selling so this will pose a problem. Other images that represent childhood would be appreciated though such as rainbows, swings, nature, stars, girls dressed in tutu or anything else you can think of.

```html
<!DOCTYPE html>
<html lang="en">
<head>
<meta charset="utf-8">
<title>Dress Up Poppet – Facebook Page Design</title>
<link rel="stylesheet" href="https://fonts.googleapis.com/css2?family=Dancing+Script:wght@700&family=Caveat:wght@700&family=Roboto:wght@400;700&display=swap">
<style>
  :root {
    --page-grey: #e9ebee;
    --panel-white: #ffffff;
    --sky-top: #bfe6f7;
    --sky-mid: #d8f0fb;
    --tone-red: #f7a3a6;
    --tone-yellow: #f8f0a0;
    --tone-green: #c4e8a4;
    --tone-blue: #a9d8f5;
    --tone-violet: #d2b8f0;
    --band-red: #f4787c;
    --band-orange: #f9a65c;
    --band-yellow: #f6ee6c;
    --band-green: #a3da6c;
    --band-blue: #82c7f0;
    --band-violet: #c69ce6;
    --brand-ink: #5b2cc4;
    --slogan-ink: #1a1a1a;
    --name-ink: #1d2a5b;
    --meta-ink: #8a8d91;
  }
  * { margin: 0; padding: 0; box-sizing: border-box; }
  html, body {
    width: 1200px; height: 541px; overflow: hidden;
    background: var(--page-grey);
  }
  .page { position: relative; width: 1200px; height: 541px; }
  .cover {
    position: absolute; left: 14px; top: 0; width: 1172px; height: 434px;
    overflow: hidden;
  }
  .cover-illustration {
    position: absolute; inset: 0;
    background:
      linear-gradient(180deg, var(--sky-top) 0%, var(--sky-mid) 30%, var(--tone-red) 48%, var(--tone-yellow) 62%, var(--tone-green) 74%, var(--tone-blue) 86%, var(--tone-violet) 100%);
  }
  .brand-title {
    position: absolute; left: 230px; width: 920px; top: 92px;
    text-align: center;
    font-family: "Dancing Script", cursive;
    font-weight: 700; font-size: 112px; line-height: 1;
    color: var(--brand-ink);
    white-space: nowrap;
  }
  .slogan {
    position: absolute; left: 380px; width: 652px; top: 252px;
    text-align: center;
    font-family: "Caveat", cursive;
    font-weight: 700; font-size: 34px; line-height: 1;
    color: var(--slogan-ink);
    white-space: nowrap;
  }
  .info-bar {
    position: absolute; left: 14px; top: 434px; width: 1172px; height: 107px;
    background: var(--panel-white);
  }
  .profile-picture {
    position: absolute; left: 44px; top: 290px; width: 232px; height: 232px;
    border: 5px solid var(--panel-white);
    box-shadow: 0 0 0 1px rgba(0,0,0,0.15);
    background: linear-gradient(135deg, var(--band-red), var(--band-orange) 25%, var(--band-yellow) 45%, var(--band-green) 62%, var(--band-blue) 80%, var(--band-violet));
    display: flex; align-items: center; justify-content: center;
    text-align: center; padding: 12px;
  }
  .profile-name {
    font-family: "Dancing Script", cursive;
    font-weight: 700; font-size: 46px; line-height: 1.05;
    color: var(--name-ink);
  }
  .page-name {
    position: absolute; left: 294px; top: 452px;
    font-family: "Roboto", sans-serif; font-weight: 700; font-size: 22px;
    color: var(--name-ink);
  }
  .page-likes {
    position: absolute; left: 294px; top: 489px;
    font-family: "Roboto", sans-serif; font-weight: 400; font-size: 15px;
    color: var(--meta-ink);
  }
</style>
</head>
<body>
<main class="page">
  <section class="cover">
    <div class="cover-illustration" role="img"
         aria-label="Whimsical sky scene with a rainbow, butterflies and soft silhouettes of girls playing"></div>
    <h1 class="brand-title">Dress Up Poppet</h1>
    <p class="slogan">Out of her dreams and into her wardrobe</p>
  </section>
  <div class="info-bar"></div>
  <div class="profile-picture">
    <span class="profile-name">Dress Up Poppet</span>
  </div>
  <h2 class="page-name">Dress Up Poppet</h2>
  <p class="page-likes">8 likes</p>
</main>
</body>
</html>
```